Bref créative
Lemon Badger
Cakes and Desserts
Bright & Fun-filled
Marla Tevison
Owner
2193 Brennick Ct.
Arvada, CO 80005
marla.tevison@postvale.net
Join us on Facebook!
I also need stationery that ties in with my business card.
Logo for cake company

```html
<!DOCTYPE html>
<html lang="en">
<head>
<meta charset="utf-8">
<title>Lemon Badger – Business Cards</title>
<link rel="stylesheet" href="https://fonts.googleapis.com/css2?family=Open+Sans:wght@400;700&family=Cinzel:wght@400&display=swap">
<style>
  :root {
    --brown: #8b4a2b;
    --pink: #e9569f;
    --pink-line: #f08cbe;
    --white: #ffffff;
    --stage: #e6d3b4;
    --label: #3a2a1c;
    --ink: #5a2f1a;
  }
  * { margin: 0; padding: 0; box-sizing: border-box; }
  html, body { width: 1200px; height: 794px; overflow: hidden; }
  body {
    background: var(--stage);
    font-family: "Open Sans", Arial, sans-serif;
    position: relative;
  }
  .card {
    position: absolute;
    width: 450px;
    height: 317px;
    border-radius: 20px;
    overflow: hidden;
    box-shadow: 0 2px 6px rgba(60, 35, 15, 0.25);
  }
  .front-a { left: 125px; top: 43px; background: var(--brown); }
  .front-b { left: 636px; top: 43px; background: var(--pink); }
  .back-a  { left: 125px; top: 408px; background: var(--white); }
  .back-b  { left: 636px; top: 408px; background: var(--brown); }

  .holder-name {
    position: absolute; top: 14px; left: 0; width: 100%;
    text-align: center; color: var(--white);
    font-weight: 700; font-size: 15px;
  }
  .band {
    position: absolute; left: 0; width: 100%;
    top: 100px; height: 96px;
    display: flex; align-items: center; justify-content: center;
  }
  .front-a .band { background: var(--white); border-bottom: 3px solid var(--pink-line); }
  .front-b .band { background: var(--brown); }
  .contact {
    position: absolute; left: 0; width: 100%;
    top: 230px; text-align: center;
    color: var(--white); font-size: 11.5px; line-height: 19px;
  }
  .contact b { font-weight: 700; }

  .brand-name {
    font-weight: 700; font-size: 30px; line-height: 1;
    white-space: nowrap; color: var(--brown);
  }
  .front-b .brand-name, .back-b .brand-name { color: var(--white); }
  .back-a .brand-name, .back-b .brand-name {
    position: absolute; left: 0; width: 100%; top: 140px;
    text-align: center; font-size: 34px;
  }
  .web {
    position: absolute; bottom: 24px; width: 100%;
    text-align: center; font-size: 11.5px; color: var(--ink);
  }

  .label {
    position: absolute; width: 450px; text-align: center;
    font-family: "Cinzel", Georgia, serif;
    font-size: 20px; letter-spacing: 2px; color: var(--label);
  }
</style>
</head>
<body>
  <section class="card front-a">
    <p class="holder-name">Marla Tevison</p>
    <div class="band"><span class="brand-name">Lemon Badger</span></div>
    <p class="contact"><b>P:</b> (720) 555-0147 | <b>E:</b> marla.tevison@postvale.net<br>www.lemonbadgercakes.com</p>
  </section>
  <p class="label" style="left:125px; top:372px;">Business Card Front A</p>

  <section class="card front-b">
    <p class="holder-name">Marla Tevison</p>
    <div class="band"><span class="brand-name">Lemon Badger</span></div>
    <p class="contact"><b>P:</b> (720) 555-0147 | <b>E:</b> marla.tevison@postvale.net<br>www.lemonbadgercakes.com</p>
  </section>
  <p class="label" style="left:636px; top:372px;">Business Card Front B</p>

  <section class="card back-a">
    <p class="brand-name">Lemon Badger</p>
    <p class="web">www.lemonbadgercakes.com</p>
  </section>
  <p class="label" style="left:125px; top:740px;">Business Card Back A</p>

  <section class="card back-b">
    <p class="brand-name">Lemon Badger</p>
  </section>
  <p class="label" style="left:636px; top:740px;">Business Card Back B</p>
</body>
</html>
```